Hartwell College Flyer Design Project

we need a flyer which promotes our business products and services, our image.

must have list of all our courses, please view our website for further information.

www.hartwellcollege.net.au

Industry/Entity Type

Business

```html
<!DOCTYPE html>
<html lang="en">
<head>
<meta charset="utf-8">
<title>Hartwell College — Courses</title>
<link rel="stylesheet" href="https://fonts.googleapis.com/css2?family=PT+Sans:wght@400;700&display=swap">
<style>
  :root {
    --frame: #e6e8ea;
    --paper: #ffffff;
    --band: #00aeef;
    --card: #5b5b5d;
    --card-text: #ffffff;
    --accent-navy: #2c4e9b;
    --accent-orange: #f0822f;
    --accent-sky: #1ba7e1;
    --accent-red: #b3312f;
    --photo-warm: #b8875a;
    --photo-cool: #6f7f96;
  }
  * { box-sizing: border-box; margin: 0; padding: 0; }
  html, body { width: 1200px; height: 857px; overflow: hidden; }
  body { background: var(--frame); font-family: "PT Sans", sans-serif; }
  .flyer {
    position: relative;
    width: 1200px; height: 857px;
    background: var(--frame);
  }
  .sheet {
    position: absolute;
    left: 14px; top: 14px;
    width: 1172px; height: 828px;
    background: var(--paper);
  }
  .band {
    position: absolute;
    left: 14px; width: 1172px; height: 41px;
    background: var(--band);
  }
  .band--top { top: 14px; }
  .band--bottom { top: 800px; }

  .course {
    position: absolute;
    width: 451px; height: 149px;
    background: var(--card);
    color: var(--card-text);
    padding: 16px 32px 0 25px;
    border-bottom: 6px solid var(--accent);
  }
  .course__title {
    font-size: 16px;
    font-weight: 700;
    line-height: 20px;
    letter-spacing: 0.1px;
  }
  .course__subtitle {
    font-size: 9px;
    font-weight: 700;
    line-height: 11px;
    margin-top: -1px;
  }
  .course__text {
    font-size: 7.4px;
    line-height: 9.55px;
    margin-top: 8px;
  }
  .course__subtitle + .course__text { margin-top: 1px; }
  .course__code {
    position: absolute;
    right: 32px; bottom: 9px;
    font-size: 7.4px;
    line-height: 9px;
  }

  .col-left { left: 82px; }
  .col-right { left: 667px; }
  .row-1 { top: 97px; }
  .row-2 { top: 269px; }
  .row-3 { top: 440px; }
  .row-4 { top: 611px; }

  .accent-navy { --accent: var(--accent-navy); }
  .accent-orange { --accent: var(--accent-orange); }
  .accent-sky { --accent: var(--accent-sky); }
  .accent-red { --accent: var(--accent-red); }

  .students-photo {
    position: absolute;
    left: 600px; top: 611px;
    width: 586px; height: 189px;
    background:
      linear-gradient(180deg, rgba(120,90,60,0.35) 0%, rgba(0,0,0,0) 40%),
      linear-gradient(90deg, var(--photo-warm) 0%, var(--photo-cool) 45%, #8a7f78 75%, #c99b6a 100%);
  }
</style>
</head>
<body>
<main class="flyer">
  <div class="sheet"></div>
  <div class="band band--top"></div>

  <article class="course col-left row-1 accent-navy">
    <h2 class="course__title">Certificate IV in Business</h2>
    <p class="course__text">Lorem ipsum dolor sit amet, consectetur adipiscing elit. Pellentesque vitae eros at sem placerat hendrerit at a neque. Donec ac libero quis eros aliquet sollicitudin nec ac metus. Maecenas tellus tellus, tempor id bibendum ut, scelerisque lacinia justo. Suspendisse libero purus, egestas id vehicula at, lacinia sit amet turpis. Proin pellentesque libero ac leo vehicula bibendum. Vivamus placerat tincidunt vulputate. Phasellus luctus, eros ut porttitor sagittis, orci metus vehicula felis, at posuere lectus sem eu ante. Aliquam pellentesque quam ut sem aliquam nec consectetur nisl porttitor. Morbi suscipit gravida lorem quis blandit. Vivamus in imperdiet erat. Aenean id est eget neque mattis ornare. Fusce lacinia mauris vitae ante rutrum ultricies. Donec porta pharetra diam eu bibendum. Aliquam erat volutpat. Mauris quis urna lacus.</p>
    <p class="course__code">BSB40207 CRICOS CODE: 073411K</p>
  </article>

  <article class="course col-left row-2 accent-orange">
    <h2 class="course__title">Diploma of Management</h2>
    <p class="course__text">Lorem ipsum dolor sit amet, consectetur adipiscing elit. Pellentesque vitae eros at sem placerat hendrerit at a neque. Donec ac libero quis eros aliquet sollicitudin nec ac metus. Maecenas tellus tellus, tempor id bibendum ut, scelerisque lacinia justo. Suspendisse libero purus, egestas id vehicula at, lacinia sit amet turpis. Proin pellentesque libero ac leo vehicula bibendum. Vivamus placerat tincidunt vulputate. Phasellus luctus, eros ut porttitor sagittis, orci metus vehicula felis, at posuere lectus sem eu ante. Aliquam pellentesque quam ut sem aliquam nec consectetur nisl porttitor. Morbi suscipit gravida lorem quis blandit. Vivamus in imperdiet erat. Aenean id est eget neque mattis ornare. Fusce lacinia mauris vitae ante rutrum ultricies. Donec porta pharetra diam eu bibendum. Aliquam erat volutpat. Mauris quis urna lacus.</p>
    <p class="course__code">BSB51107 CRICOS CODE:072723B</p>
  </article>

  <article class="course col-left row-3 accent-sky">
    <h2 class="course__title">Advance Diploma of Management</h2>
    <p class="course__text">Lorem ipsum dolor sit amet, consectetur adipiscing elit. Pellentesque vitae eros at sem placerat hendrerit at a neque. Donec ac libero quis eros aliquet sollicitudin nec ac metus. Maecenas tellus tellus, tempor id bibendum ut, scelerisque lacinia justo. Suspendisse libero purus, egestas id vehicula at, lacinia sit amet turpis. Proin pellentesque libero ac leo vehicula bibendum. Vivamus placerat tincidunt vulputate. Phasellus luctus, eros ut porttitor sagittis, orci metus vehicula felis, at posuere lectus sem eu ante. Aliquam pellentesque quam ut sem aliquam nec consectetur nisl porttitor. Morbi suscipit gravida lorem quis blandit. Vivamus in imperdiet erat. Aenean id est eget neque mattis ornare. Fusce lacinia mauris vitae ante rutrum ultricies. Donec porta pharetra diam eu bibendum. Aliquam erat volutpat. Mauris quis urna lacus.</p>
    <p class="course__code">BSB60407 CRICOS CODE: 073412J</p>
  </article>

  <article class="course col-left row-4 accent-red">
    <h2 class="course__title">Certificate III in Hospitality</h2>
    <p class="course__subtitle">(Commercial Cookery)</p>
    <p class="course__text">Lorem ipsum dolor sit amet, consectetur adipiscing elit. Pellentesque vitae eros at sem placerat hendrerit at a neque. Donec ac libero quis eros aliquet sollicitudin nec ac metus. Maecenas tellus tellus, tempor id bibendum ut, scelerisque lacinia justo. Suspendisse libero purus, egestas id vehicula at, lacinia sit amet turpis. Proin pellentesque libero ac leo vehicula bibendum. Vivamus placerat tincidunt vulputate. Phasellus luctus, eros ut porttitor sagittis, orci metus vehicula felis, at posuere lectus sem eu ante. Aliquam pellentesque quam ut sem aliquam nec consectetur nisl porttitor. Morbi suscipit gravida lorem quis blandit. Vivamus in imperdiet erat. Aenean id est eget neque mattis ornare. Fusce lacinia mauris vitae ante rutrum ultricies. Donec porta pharetra diam eu bibendum. Aliquam erat volutpat. Mauris quis urna lacus.</p>
    <p class="course__code">SIT30807 CRICOS CODE:067958C</p>
  </article>

  <article class="course col-right row-1 accent-navy">
    <h2 class="course__title">Certificate III in Hospitality(Patisserie)</h2>
    <p class="course__text">Lorem ipsum dolor sit amet, consectetur adipiscing elit. Pellentesque vitae eros at sem placerat hendrerit at a neque. Donec ac libero quis eros aliquet sollicitudin nec ac metus. Maecenas tellus tellus, tempor id bibendum ut, scelerisque lacinia justo. Suspendisse libero purus, egestas id vehicula at, lacinia sit amet turpis. Proin pellentesque libero ac leo vehicula bibendum. Vivamus placerat tincidunt vulputate. Phasellus luctus, eros ut porttitor sagittis, orci metus vehicula felis, at posuere lectus sem eu ante. Aliquam pellentesque quam ut sem aliquam nec consectetur nisl porttitor. Morbi suscipit gravida lorem quis blandit. Vivamus in imperdiet erat. Aenean id est eget neque mattis ornare. Fusce lacinia mauris vitae ante rutrum ultricies. Donec porta pharetra diam eu bibendum. Aliquam erat volutpat. Mauris quis urna lacus.</p>
    <p class="course__code">SIT31107 CRICOS CODE:0707586G</p>
  </article>

  <article class="course col-right row-2 accent-orange">
    <h2 class="course__title">Certificate IV in Hospitality</h2>
    <p class="course__subtitle">(Commercial Cookery)</p>
    <p class="course__text">Lorem ipsum dolor sit amet, consectetur adipiscing elit. Pellentesque vitae eros at sem placerat hendrerit at a neque. Donec ac libero quis eros aliquet sollicitudin nec ac metus. Maecenas tellus tellus, tempor id bibendum ut, scelerisque lacinia justo. Suspendisse libero purus, egestas id vehicula at, lacinia sit amet turpis. Proin pellentesque libero ac leo vehicula bibendum. Vivamus placerat tincidunt vulputate. Phasellus luctus, eros ut porttitor sagittis, orci metus vehicula felis, at posuere lectus sem eu ante. Aliquam pellentesque quam ut sem aliquam nec consectetur nisl porttitor. Morbi suscipit gravida lorem quis blandit. Vivamus in imperdiet erat. Aenean id est eget neque mattis ornare. Fusce lacinia mauris vitae ante rutrum ultricies. Donec porta pharetra diam eu bibendum. Aliquam erat volutpat. Mauris quis urna lacus.</p>
    <p class="course__code">SIT40407 CRICOS CODE:071187G</p>
  </article>

  <article class="course col-right row-3 accent-sky">
    <h2 class="course__title">Diploma of Hospitality</h2>
    <p class="course__text">Lorem ipsum dolor sit amet, consectetur adipiscing elit. Pellentesque vitae eros at sem placerat hendrerit at a neque. Donec ac libero quis eros aliquet sollicitudin nec ac metus. Maecenas tellus tellus, tempor id bibendum ut, scelerisque lacinia justo. Suspendisse libero purus, egestas id vehicula at, lacinia sit amet turpis. Proin pellentesque libero ac leo vehicula bibendum. Vivamus placerat tincidunt vulputate. Phasellus luctus, eros ut porttitor sagittis, orci metus vehicula felis, at posuere lectus sem eu ante. Aliquam pellentesque quam ut sem aliquam nec consectetur nisl porttitor. Morbi suscipit gravida lorem quis blandit. Vivamus in imperdiet erat. Aenean id est eget neque mattis ornare. Fusce lacinia mauris vitae ante rutrum ultricies. Donec porta pharetra diam eu bibendum. Aliquam erat volutpat. Mauris quis urna lacus.</p>
    <p class="course__code">SIT50307 CRICOS CODE:067959B</p>
  </article>

  <div class="students-photo" role="img" aria-label="Photo of smiling students seated in a classroom, one holding books in the foreground"></div>

  <div class="band band--bottom"></div>
</main>
</body>
</html>
```